Music portal needs a sleek mobile app design

We need an innovative, cutting edge design for our mobile app for www.tunelofthub.net . LOFTHUB Music is a platform that lets independent musicians upload and share their music for free. Music lovers can discover new music too.

If you visit the website, you'll get an idea of our brand colors and theme. im attaching the logo and our new discover page layout. We use "din Next LT pro" as our brand font.

We are looking for an app optimized for iOS, but can be used on Android and windows too.

Im looking for a design that flows and navigates with user intuition and is sleek, flat style in nature and has Similar apps are wavecrate, tunebarn and blendsky.

Here are some ideas we like, but please dont copy. Come up with something similar in 'feel'

https://www.folioplace.net/gallery/B-TUNE-UP-Music-application/4421930

https://pixelpost.net/shots/7730582-Music-App

The most important pages/ screens for us are:
- The discover screen
- The login and sign up screens
- The splash screen
- The track player screen
- The use profile page screen
Updates

It seems no design has come close to what I was looking for so I will be requesting a refund and withdrawing this project. Thanks for your effort

Target Market(s)

music, music app, wavecrate, lofthub music, music app design

Colors
f78f20
ffcf3e
ffffff
000000

Requirements
Must have
• a sleek easy to use navigation- please create an account on tunelofthub.net to see how the site works.
Nice to have
• Sleek screen to screen transitions
Should not have
• no 3d designs. Flat design only

```html
<!DOCTYPE html>
<html lang="en">
<head>
<meta charset="utf-8">
<title>LOFTHUB Music App – Screen Mockup Samples</title>
<link rel="stylesheet" href="https://fonts.googleapis.com/css2?family=Barlow:ital,wght@0,400;0,600;0,700;0,800;1,700;1,800&display=swap">
<style>
  :root{
    --orange:#fda712;
    --orange-deep:#f78f20;
    --gold:#ffcf3e;
    --sand:#e2c873;
    --white:#ffffff;
    --black:#000000;
    --ink:#111111;
    --panel:#1b1b1b;
    --grey:#8a8a8a;
    --grey-dark:#5e5e5e;
    --rule:#6f6f6f;
    --font:"Barlow", Arial, sans-serif;
  }
  *{box-sizing:border-box;margin:0;padding:0}
  html,body{width:960px;height:1200px;overflow:hidden}
  body{
    position:relative;font-family:var(--font);color:var(--white);
    background:radial-gradient(ellipse 900px 700px at 55% 10%, #2e2e2e 0%, #151515 55%, #060606 100%);
  }
  .connectors{position:absolute;inset:0;width:960px;height:1200px}
  .connectors path{fill:none;stroke:var(--rule);stroke-width:1}

  /* board titles */
  .board-brand{position:absolute;left:83px;top:260px;width:230px}
  .brand-square{width:146px;height:134px;border:3px solid var(--orange);background:var(--black)}
  .brand-name{margin-top:10px;font-size:40px;font-weight:800;font-style:italic;letter-spacing:.5px;line-height:1}
  .brand-line{font-weight:800;font-style:italic;color:var(--grey-dark);line-height:.95}
  .brand-line.music{font-size:34px;margin-left:-8px;margin-top:2px}
  .brand-line.app{font-size:40px;margin-left:-14px}
  .brand-sub{margin-top:12px;margin-left:-16px;font-size:18px;font-weight:700;font-style:italic;color:var(--grey-dark);line-height:1.15}

  .section-title{position:absolute;font-size:18px;font-weight:700;font-style:italic;color:var(--grey);letter-spacing:.4px;white-space:nowrap;transform:translateX(-50%)}

  /* phone screens */
  .screen{position:absolute;width:197px;height:351px;overflow:hidden;background:var(--panel)}
  .status-bar{position:absolute;left:0;top:0;width:100%;height:13px;display:flex;justify-content:space-between;align-items:center;padding:0 5px;font-size:6px;color:var(--white);background:rgba(0,0,0,.55);z-index:2}
  .status-bar .time{font-weight:600}
  .photo{position:absolute;inset:0}
  .logo-lockup{position:absolute;left:50%;transform:translateX(-50%);display:flex;flex-direction:column;align-items:center}
  .logo-square{width:49px;height:46px;border:2px solid var(--orange);background:rgba(0,0,0,.85)}
  .logo-name{margin-top:4px;font-size:13px;font-weight:800;color:var(--white);letter-spacing:.3px}
  .loader{position:absolute;left:50%;transform:translateX(-50%);display:flex;flex-direction:column;align-items:center;font-size:4.5px;color:var(--orange)}
  .splash-band{position:absolute;left:0;bottom:0;width:100%;height:40px;background:var(--orange);display:flex;align-items:center;justify-content:space-between;padding:0 10px 0 42px}
  .splash-band p{font-size:6px;line-height:1.25;color:var(--ink);width:92px}
  .pager{display:flex;gap:4px}
  .pager i{width:6px;height:6px;border-radius:50%;background:var(--ink);border:1px solid var(--ink)}
  .pager i.off{background:transparent}
  .headline{position:absolute;right:10px;top:36px;text-align:right;font-size:22px;font-weight:600;line-height:.95;color:var(--sand)}

  /* login */
  .login{background:linear-gradient(180deg,#2c2c2c 0%,#1a1a1a 55%,#141414 100%)}
  .login-form{position:absolute;left:52px;top:214px;width:92px}
  .field-label{font-size:5.5px;color:var(--white);padding-bottom:2px;border-bottom:1px solid var(--grey-dark)}
  .field{margin-top:10px;height:16px;border:1px solid var(--orange);border-radius:4px;font-size:5.5px;color:var(--white);display:flex;align-items:center;padding-left:6px}
  .forgot{margin-top:5px;text-align:right;font-size:5px;color:var(--white)}
  .signup-band{position:absolute;left:0;bottom:0;width:100%;height:38px;background:var(--orange);display:flex;align-items:center;justify-content:center;font-size:9px;font-weight:700;color:var(--ink)}

  /* profile */
  .profile{background:var(--orange)}
  .profile .status-bar{background:var(--orange)}
  .title-bar{position:absolute;top:13px;left:0;width:100%;height:19px;background:var(--white);color:var(--ink);font-size:8px;display:flex;align-items:center;justify-content:center}
  .avatar{position:absolute;left:59px;top:52px;width:82px;height:82px;border-radius:50%;border:3px solid var(--white);background:radial-gradient(circle at 45% 40%,#d9a7a2,#8a6a6a 60%,#4e4b52)}
  .profile-name{position:absolute;top:138px;width:100%;text-align:center;font-size:7px;color:var(--white)}
  .round-btn{position:absolute;top:119px;width:24px;height:24px;border-radius:50%;border:1px solid var(--white);display:flex;align-items:center;justify-content:center}
  .now-strip{position:absolute;left:0;top:177px;width:100%;height:37px;background:var(--black);padding:4px 6px}
  .now-strip .label{font-size:5px;color:var(--white);margin-left:72px}
  .controls-mini{position:absolute;left:6px;top:12px;display:flex;gap:4px}
  .controls-mini span{width:16px;height:16px;border-radius:50%;border:1px solid var(--orange);display:flex;align-items:center;justify-content:center}
  .track-mini{position:absolute;left:78px;top:22px;font-size:4px;color:var(--orange)}
  .track-mini::after{content:"";display:block;margin-top:2px;width:58px;height:1px;background:var(--orange)}
  .bars-mini{position:absolute;right:8px;top:13px}
  .action-grid{position:absolute;left:0;top:214px;width:100%;height:119px;display:grid;grid-template-columns:repeat(3,1fr);grid-template-rows:repeat(2,1fr)}
  .action{display:flex;flex-direction:column;align-items:center;justify-content:center;gap:4px;border-right:1px solid #ffc45a;border-bottom:1px solid #ffc45a;font-size:5px;color:var(--white)}
  .action:nth-child(3n){border-right:none}
  .tab-bar{position:absolute;left:0;bottom:0;width:100%;height:19px;background:var(--black);display:flex;align-items:center;justify-content:center}

  /* now playing */
  .player{background:linear-gradient(180deg,#3a3a3a 0%,#262626 60%,#1c1c1c 100%)}
  .player-top{position:absolute;top:13px;left:0;width:100%;height:18px;display:flex;justify-content:flex-end;align-items:center;padding-right:10px}
  .song-title{position:absolute;top:46px;width:100%;text-align:center;font-size:17px;font-weight:700;color:var(--orange)}
  .disc{position:absolute;left:46px;top:78px;width:105px;height:105px;border-radius:50%;border:2px solid var(--orange);background:radial-gradient(circle at 50% 45%,#6a6a6a,#2c2c2c 75%)}
  .artist{position:absolute;top:192px;width:100%;text-align:center;font-size:9px;color:var(--orange)}
  .progress{position:absolute;left:18px;top:236px;width:161px;height:2px;background:#555}
  .progress::before{content:"";position:absolute;left:0;top:0;width:64%;height:2px;background:var(--orange)}
  .progress::after{content:"";position:absolute;left:98px;top:-4px;width:10px;height:10px;border-radius:50%;background:var(--orange)}
  .player-controls{position:absolute;top:262px;width:100%;display:flex;justify-content:center;align-items:center;gap:22px}
  .play-btn{width:18px;height:18px;border-radius:50%;background:var(--orange);display:flex;align-items:center;justify-content:center}
  .player-foot{position:absolute;left:0;bottom:0;width:100%;height:34px;background:#1a1a1a;display:flex;justify-content:space-between;align-items:center;padding:0 16px}
</style>
</head>
<body>

<svg class="connectors" viewBox="0 0 960 1200" aria-hidden="true">
  <path d="M265 46 H505"/>
  <path d="M692 46 H768 V82"/>
  <path d="M265 46 V765 H383"/>
  <path d="M265 220 H384"/>
  <path d="M544 1118 V1051 H350"/>
</svg>

<div class="board-brand">
  <div class="brand-square"></div>
  <div class="brand-name">LOFTHUB</div>
  <div class="brand-line music">MUSIC</div>
  <div class="brand-line app">APP</div>
  <div class="brand-sub">SCREEN MOCKUP<br>SAMPLES</div>
</div>

<div class="section-title" style="left:600px;top:36px">SPLASH SCREENS</div>
<div class="section-title" style="left:485px;top:500px">LOGIN SCREEN</div>
<div class="section-title" style="left:700px;top:500px">PROFILE SCREEN</div>
<div class="section-title" style="left:541px;top:1130px">NOW PLAYING</div>

<!-- Splash screen one -->
<section class="screen splash" style="left:386px;top:85px">
  <div class="photo" role="img" aria-label="Photo of a smiling music fan wearing headphones" style="background:linear-gradient(160deg,#8a7a55 0%,#5e5236 45%,#3a3a40 100%)"></div>
  <div class="status-bar"><span>●●●○○ CELLA</span><span class="time">4:21 PM</span><span>100%</span></div>
  <div class="headline">SHARE<br>THE<br>MUSIC</div>
  <div class="logo-lockup" style="top:129px"><div class="logo-square"></div><div class="logo-name">LOFTHUB</div></div>
  <div class="loader" style="top:276px">
    <svg width="60" height="10" viewBox="0 0 60 10"><path d="M0 5 H12 L16 2 L20 8 L26 1 L32 9 L36 4 L42 6 H60" fill="none" stroke="#fda712" stroke-width="1"/></svg>
    <span>Loading</span>
  </div>
  <div class="splash-band">
    <p>Share, download and post music from any device</p>
    <div class="pager"><i></i><i class="off"></i><i></i></div>
  </div>
</section>

<!-- Splash screen two -->
<section class="screen splash" style="left:602px;top:85px">
  <div class="photo" role="img" aria-label="Dim photo of a dancer in motion" style="background:linear-gradient(170deg,#3a3a3a 0%,#262626 50%,#1a1a1a 100%)"></div>
  <div class="status-bar"><span>●●●○○ CELLA</span><span class="time">4:21 PM</span><span>100%</span></div>
  <div class="logo-lockup" style="top:129px"><div class="logo-square"></div><div class="logo-name">LOFTHUB</div></div>
  <div class="loader" style="top:276px">
    <svg width="60" height="10" viewBox="0 0 60 10"><path d="M0 5 H12 L16 2 L20 8 L26 1 L32 9 L36 4 L42 6 H60" fill="none" stroke="#fda712" stroke-width="1"/></svg>
    <span>Loading</span>
  </div>
  <div class="splash-band">
    <p>Build a fanbase and collaborate with new artists</p>
    <div class="pager"><i></i><i class="off"></i><i></i></div>
  </div>
</section>

<!-- Login screen -->
<section class="screen login" style="left:385px;top:544px">
  <div class="status-bar"><span>●●●○○ CELLA</span><span class="time">4:21 PM</span><span>100%</span></div>
  <div class="logo-lockup" style="top:130px"><div class="logo-square"></div><div class="logo-name">LOFTHUB</div></div>
  <form class="login-form">
    <div class="field-label">Login</div>
    <div class="field">Username</div>
    <div class="field">Password</div>
    <div class="forgot">forgot?</div>
  </form>
  <div class="signup-band">SIGN UP</div>
</section>

<!-- Profile screen -->
<section class="screen profile" style="left:602px;top:544px">
  <div class="status-bar"><span>●●●○○ CELLA</span><span class="time">4:21 PM</span><span>100%</span></div>
  <div class="title-bar">Profile</div>
  <svg style="position:absolute;left:8px;top:40px" width="22" height="22" viewBox="0 0 24 24" aria-hidden="true"><path fill="#fff" d="M10 1h4l.6 3 2.2 1 2.6-1.7 2.8 2.8L20.5 8.7l1 2.3 3 .5v4l-3 .6-1 2.3 1.7 2.6-2.8 2.8-2.6-1.7-2.2 1-.6 3h-4l-.6-3-2.3-1-2.5 1.7-2.8-2.8L3.5 18l-1-2.3-3-.6v-4l3-.5 1-2.3L1.8 5.1l2.8-2.8L7.1 4l2.3-1z"/><circle cx="12" cy="13" r="4" fill="#fda712"/></svg>
  <svg style="position:absolute;right:8px;top:40px" width="22" height="18" viewBox="0 0 22 18" aria-hidden="true"><g fill="#fff"><rect x="0" y="0" width="4" height="3"/><rect x="6" y="0" width="16" height="3"/><rect x="0" y="5" width="4" height="3"/><rect x="6" y="5" width="16" height="3"/><rect x="0" y="10" width="4" height="3"/><rect x="6" y="10" width="16" height="3"/><rect x="0" y="15" width="4" height="3"/><rect x="6" y="15" width="16" height="3"/></g></svg>
  <div class="avatar" role="img" aria-label="Profile photo of the user"></div>
  <div class="round-btn" style="left:31px"><svg width="10" height="10" viewBox="0 0 10 10" aria-hidden="true"><path d="M2 8 L8 2" stroke="#fff" stroke-width="2.5" stroke-linecap="round"/></svg></div>
  <div class="round-btn" style="left:143px"><svg width="12" height="10" viewBox="0 0 12 10" aria-hidden="true"><g stroke="#fff" stroke-width="1"><path d="M1 4v2M3 2v6M5 0v10M7 2v6M9 3v4M11 4v2"/></g></svg></div>
  <div class="profile-name">Mara Quinn</div>
  <div class="now-strip">
    <div class="label">Now playing</div>
    <div class="controls-mini">
      <span><svg width="8" height="6" viewBox="0 0 8 6"><path d="M4 0v6L0 3zM8 0v6L4 3z" fill="#fda712"/></svg></span>
      <span><svg width="6" height="6" viewBox="0 0 6 6"><path d="M0 0h2v6H0zM4 0h2v6H4z" fill="#fda712"/></svg></span>
      <span><svg width="8" height="6" viewBox="0 0 8 6"><path d="M0 0v6l4-3zM4 0v6l4-3z" fill="#fda712"/></svg></span>
    </div>
    <div class="track-mini">Only One - mara quinn - edit</div>
    <svg class="bars-mini" width="20" height="12" viewBox="0 0 20 12" aria-hidden="true"><g fill="#fda712"><rect x="0" y="6" width="2" height="6"/><rect x="3" y="2" width="2" height="10"/><rect x="6" y="4" width="2" height="8"/><rect x="9" y="0" width="2" height="12"/><rect x="12" y="5" width="2" height="7"/><rect x="15" y="3" width="2" height="9"/><rect x="18" y="7" width="2" height="5"/></g></svg>
  </div>
  <div class="action-grid">
    <div class="action"><svg width="26" height="24" viewBox="0 0 26 24" aria-hidden="true"><path d="M3 16V12a10 10 0 0 1 20 0v4" fill="none" stroke="#fff" stroke-width="2.5"/><rect x="1" y="13" width="6" height="10" rx="2" fill="#fff"/><rect x="19" y="13" width="6" height="10" rx="2" fill="#fff"/></svg>Playlist</div>
    <div class="action"><svg width="26" height="24" viewBox="0 0 26 24" aria-hidden="true"><g fill="#fff"><circle cx="9" cy="7" r="5"/><path d="M0 22a9 8 0 0 1 18 0z"/><circle cx="19" cy="8" r="4"/><path d="M15 14a7 6 0 0 1 11 8h-7z"/></g></svg>Following</div>
    <div class="action"><svg width="24" height="24" viewBox="0 0 24 24" aria-hidden="true"><g fill="#fff"><circle cx="19" cy="5" r="4"/><circle cx="5" cy="12" r="4"/><circle cx="19" cy="19" r="4"/></g><path d="M19 5L5 12l14 7" fill="none" stroke="#fff" stroke-width="2"/></svg>Share</div>
    <div class="action"><svg width="26" height="22" viewBox="0 0 26 22" aria-hidden="true"><path d="M13 22L2 11A6 6 0 0 1 13 4a6 6 0 0 1 11 7z" fill="#fff"/></svg>Likes</div>
    <div class="action"><svg width="26" height="22" viewBox="0 0 26 22" aria-hidden="true"><rect x="2" y="2" width="18" height="16" rx="1" fill="#fff"/><path d="M20 6h3v7h-3" fill="none" stroke="#fff" stroke-width="2"/><rect x="0" y="19" width="24" height="2" fill="#fff"/></svg>Groups</div>
    <div class="action"><svg width="28" height="24" viewBox="0 0 28 24" aria-hidden="true"><path d="M2 2h16v11H8l-4 4v-4H2z" fill="#fff"/><path d="M20 7h6v10h-2v4l-4-4h-8v-2h8z" fill="#fff"/></svg>Comment</div>
  </div>
  <div class="tab-bar"><svg width="14" height="14" viewBox="0 0 14 14" aria-hidden="true"><path d="M7 1v8M4 4l3-3 3 3" fill="none" stroke="#fda712" stroke-width="1.5"/><path d="M2 7v6h10V7" fill="none" stroke="#fda712" stroke-width="1.5"/></svg></div>
</section>

<!-- Now playing screen -->
<section class="screen player" style="left:150px;top:770px">
  <div class="status-bar"><span>●●●○○ CELLA</span><span class="time">4:21 PM</span><span>100%</span></div>
  <div class="player-top"><svg width="14" height="11" viewBox="0 0 14 11" aria-hidden="true"><g fill="#fda712"><rect x="0" y="0" width="2" height="2"/><rect x="4" y="0" width="10" height="2"/><rect x="0" y="4.5" width="2" height="2"/><rect x="4" y="4.5" width="10" height="2"/><rect x="0" y="9" width="2" height="2"/><rect x="4" y="9" width="10" height="2"/></g></svg></div>
  <div class="song-title">Let's Go</div>
  <div class="disc" role="img" aria-label="Album artwork of the current track"></div>
  <div class="artist">Tessa Vale</div>
  <div class="progress"></div>
  <div class="player-controls">
    <svg width="14" height="9" viewBox="0 0 14 9" aria-hidden="true"><path d="M7 0v9L0 4.5zM14 0v9L7 4.5z" fill="#fda712"/></svg>
    <div class="play-btn"><svg width="7" height="7" viewBox="0 0 6 6"><path d="M0 0h2v6H0zM4 0h2v6H4z" fill="#111"/></svg></div>
    <svg width="14" height="9" viewBox="0 0 14 9" aria-hidden="true"><path d="M0 0v9l7-4.5zM7 0v9l7-4.5z" fill="#fda712"/></svg>
  </div>
  <div class="player-foot">
    <svg width="14" height="10" viewBox="0 0 14 10" aria-hidden="true"><path d="M3 2h9v5M11 8H2V3" fill="none" stroke="#fff" stroke-width="1.3"/></svg>
    <svg width="14" height="10" viewBox="0 0 14 10" aria-hidden="true"><path d="M0 2h4l6 6h4M0 8h4l6-6h4" fill="none" stroke="#fff" stroke-width="1.3"/></svg>
  </div>
</section>

</body>
</html>
```